We need a web page design for a new company called "Brindle". We provide an innovative music sharing mobile application that allows music listeners to share their music without paying for a monthly subscription. We would like to incorporate the attached logo and color scheme. The final design should communicate music gifting and sharing.

Industry/Entity Type

It Company

```html
<!DOCTYPE html>
<html lang="en">
<head>
<meta charset="utf-8">
<title>Brindle — Own the Music</title>
<link rel="stylesheet" href="https://fonts.googleapis.com/css2?family=Lato:wght@300;400;700;900&family=Oswald:wght@400;500&display=swap">
<style>
:root{
  --green:#56a10b;
  --orange:#ff6c40;
  --white:#ffffff;
  --grey-text:#9a9a9a;
  --dark-text:#333333;
  --border:#d6d6d6;
  --footer:#1e1e1e;
}
*{margin:0;padding:0;box-sizing:border-box}
html,body{width:845px;height:1200px;overflow:hidden}
body{position:relative;font-family:'Lato',sans-serif;background:var(--white)}
.abs{position:absolute}

.hero{left:0;top:0;width:845px;height:410px;background:var(--green)}
.brand{left:133px;top:14px;display:flex;align-items:center;gap:7px}
.brand-dot{width:26px;height:26px;border-radius:50%;background:var(--white)}
.brand-name{color:var(--white);font-size:28px;font-weight:400;line-height:1}
.nav-line{left:133px;top:63px;width:579px;height:1px;background:rgba(255,255,255,.75)}
.btn{top:21px;width:60px;height:23px;font-family:'Oswald',sans-serif;font-size:10px;display:flex;align-items:center;justify-content:center;text-transform:uppercase}
.btn-login{left:579px;background:var(--white);color:var(--green)}
.btn-signup{left:652px;border:1px solid var(--white);color:var(--white)}
.hero-title{left:133px;top:139px;width:340px;color:var(--white);font-size:21px;font-weight:300;line-height:26px;white-space:nowrap}
.hero-sub{left:133px;top:211px;width:300px;color:var(--white);font-size:10.5px;font-weight:900;line-height:14px;text-transform:uppercase}
.store-badge{top:272px;height:35px;background:#111;border:1.5px solid var(--white);border-radius:4px}
.badge-a{left:133px;width:102px}
.badge-b{left:260px;width:108px}
.hero-phones{left:497px;top:111px;width:215px;height:250px;border-radius:18px;background:linear-gradient(160deg,#1c1c1c 0%,#2a4d7a 45%,#e8e8e8 100%)}

.section-title{left:0;width:845px;text-align:center;font-size:19px;font-weight:300}
.section-text{left:188px;width:469px;text-align:center;font-size:11px;line-height:13.5px;font-weight:300}

.features .section-title{top:438px;color:var(--green)}
.features .section-text{top:480px;color:var(--grey-text)}
.feature{top:536px;width:100px;display:flex;flex-direction:column;align-items:center}
.feature-ring{width:85px;height:85px;border:1px solid var(--green);border-radius:50%;display:flex;align-items:center;justify-content:center}
.feature-label{margin-top:12px;font-family:'Oswald',sans-serif;font-weight:500;font-size:11px;line-height:12.5px;color:var(--green);text-align:center;text-transform:uppercase}

.how{left:0;top:685px;width:845px;height:354px;background:var(--orange)}
.how .section-title{top:27px;color:var(--white)}
.how .section-text{top:67px;color:var(--white);font-weight:400}
.select{left:310px;top:115px;width:121px;height:30px;background:var(--white);color:var(--orange);font-size:12px;display:flex;align-items:center;justify-content:space-between;padding:0 10px 0 8px}
.caret{width:0;height:0;border-left:4px solid transparent;border-right:4px solid transparent;border-top:5px solid var(--orange)}
.gift-btn{left:449px;top:115px;width:85px;height:30px;border:1px solid var(--white);color:var(--white);font-size:12px;font-weight:700;display:flex;align-items:center;justify-content:center;gap:12px}
.hands-photo{left:240px;top:164px;width:364px;height:190px;border-radius:20px 20px 0 0;background:linear-gradient(180deg,#f4f4f4 0%,#e9c9b3 60%,#d9a98f 100%)}

.contact .section-title{top:1059px;color:var(--dark-text)}
.contact-box{top:1104px;width:181px;height:46px;border:1px solid var(--border);display:flex;align-items:center;padding-left:14px;gap:14px;color:#9a9a9a}
.box-address{left:133px}
.box-phone{left:332px}
.box-mail{left:531px}
.contact-small{font-size:8px;line-height:10.5px;color:#666}
.contact-large{font-size:15px;font-weight:300}

.footer{left:0;top:1176px;width:845px;height:24px;background:var(--footer)}
.copyright{left:133px;top:7px;color:var(--white);font-size:8px}
.social{top:7px;width:10px;height:10px;border-radius:50%;background:var(--white)}
</style>
</head>
<body>

<header class="hero abs">
  <div class="brand abs"><span class="brand-dot"></span><span class="brand-name">Brindle</span></div>
  <a class="btn btn-login abs">Login</a>
  <a class="btn btn-signup abs">Sign up</a>
  <div class="nav-line abs"></div>
  <h1 class="hero-title abs">We provide an innovative music<br>sharing mobile application</h1>
  <p class="hero-sub abs">Neque porro quisquam est qui dolorem ipsum quia dolor sit amet,</p>
  <div class="store-badge badge-a abs"></div>
  <div class="store-badge badge-b abs"></div>
  <div class="hero-phones abs" role="img" aria-label="Two smartphones showing the music app's library and search screens"></div>
</header>

<section class="features">
  <h2 class="section-title abs">Mobile app Features</h2>
  <p class="section-text abs">Lorem ipsum dolor sit amet, consectetur adipiscing elit, sed do eiusmod tempor incididunt ut labore et dolore magna aliqua. Ut enim ad minim veniam, quis nostrud exercitation ullamco</p>

  <div class="feature abs" style="left:125px">
    <div class="feature-ring">
      <svg width="46" height="32" viewBox="0 0 46 32" fill="none" stroke="var(--green)" stroke-width="2.5"><rect x="6" y="2" width="38" height="20"/><rect x="2" y="8" width="38" height="22" fill="var(--green)"/><circle cx="21" cy="19" r="6" stroke="#fff"/><text x="21" y="23" font-size="10" font-family="Lato" font-weight="900" fill="#fff" stroke="none" text-anchor="middle">$</text></svg>
    </div>
    <div class="feature-label">No monthly<br>fees</div>
  </div>

  <div class="feature abs" style="left:248px">
    <div class="feature-ring">
      <svg width="44" height="40" viewBox="0 0 44 40" fill="var(--green)" stroke="var(--green)" stroke-width="3"><line x1="8" y1="8" x2="22" y2="20"/><line x1="36" y1="12" x2="22" y2="20"/><line x1="22" y1="20" x2="14" y2="34"/><circle cx="8" cy="8" r="5"/><circle cx="36" cy="12" r="5"/><circle cx="22" cy="20" r="5"/><circle cx="14" cy="34" r="5"/></svg>
    </div>
    <div class="feature-label">Share<br>your favourite</div>
  </div>

  <div class="feature abs" style="left:372px">
    <div class="feature-ring">
      <svg width="32" height="34" viewBox="0 0 32 34" fill="var(--green)"><path d="M16 8 C10 0 4 4 9 8Z M16 8 C22 0 28 4 23 8Z"/><rect x="1" y="9" width="30" height="7"/><rect x="3" y="17" width="26" height="17"/><rect x="14" y="9" width="4" height="25" fill="#fff"/></svg>
    </div>
    <div class="feature-label">Send<br>music gift</div>
  </div>

  <div class="feature abs" style="left:496px">
    <div class="feature-ring">
      <svg width="38" height="34" viewBox="0 0 38 34" fill="var(--green)"><rect x="0" y="2" width="20" height="4"/><rect x="0" y="10" width="20" height="4"/><rect x="0" y="18" width="14" height="4"/><rect x="0" y="26" width="14" height="4"/><rect x="26" y="2" width="3" height="24"/><circle cx="23" cy="27" r="6"/><path d="M29 2 L37 8 L29 10Z"/></svg>
    </div>
    <div class="feature-label">Create<br>playlist</div>
  </div>

  <div class="feature abs" style="left:619px">
    <div class="feature-ring">
      <svg width="34" height="34" viewBox="0 0 34 34" fill="none" stroke="var(--green)" stroke-width="2.5"><rect x="9" y="2" width="23" height="23"/><path d="M2 9 V32 H25"/><path d="M24 8 V19" /><circle cx="21" cy="19" r="3" fill="var(--green)"/><path d="M24 8 L17 10 V21"/><circle cx="14" cy="21" r="3" fill="var(--green)"/></svg>
    </div>
    <div class="feature-label">New<br>albums</div>
  </div>
</section>

<section class="how abs">
  <h2 class="section-title abs">How it works</h2>
  <p class="section-text abs">Lorem ipsum dolor sit amet, consectetur adipiscing elit, sed do eiusmod tempor incididunt ut labore et dolore magna aliqua. Ut enim ad minim veniam, quis nostrud exercitation ullamco</p>
  <div class="select abs"><span>Select Listen</span><span class="caret"></span></div>
  <div class="gift-btn abs">
    <svg width="15" height="16" viewBox="0 0 32 34" fill="#fff"><path d="M16 8 C10 0 4 4 9 8Z M16 8 C22 0 28 4 23 8Z"/><rect x="1" y="9" width="30" height="7"/><rect x="3" y="17" width="26" height="17"/><rect x="14" y="9" width="4" height="25" fill="var(--orange)"/></svg>
    <span>GIFT</span>
  </div>
  <div class="hands-photo abs" role="img" aria-label="Two hands holding a white smartphone sideways, playing a music video"></div>
</section>

<section class="contact">
  <h2 class="section-title abs">Get in Touch With Us!</h2>
  <div class="contact-box box-address abs">
    <svg width="11" height="15" viewBox="0 0 11 15"><path d="M5.5 0A5.5 5.5 0 0 0 0 5.5C0 9.5 5.5 15 5.5 15S11 9.5 11 5.5A5.5 5.5 0 0 0 5.5 0Z" fill="#999"/><circle cx="5.5" cy="5.5" r="2" fill="#fff"/></svg>
    <span class="contact-small">Lorem ipsum dolor sit amet, con-<br>sectetur adipiscing elit,</span>
  </div>
  <div class="contact-box box-phone abs">
    <svg width="12" height="13" viewBox="0 0 12 13"><path d="M2 0 L4.5 3 L3 5 C4 7.5 5.5 9 8 10 L10 8.5 L12 11 L10 13 C4.5 12 0.5 7.5 0 2Z" fill="#999"/></svg>
    <span class="contact-large">+000-000-00</span>
  </div>
  <div class="contact-box box-mail abs">
    <svg width="15" height="11" viewBox="0 0 15 11"><rect width="15" height="11" fill="#999"/><path d="M0 0 L7.5 6 L15 0" stroke="#fff" fill="none"/></svg>
    <span class="contact-large">info@brindle.com</span>
  </div>
</section>

<footer class="footer abs">
  <p class="copyright abs">Copy Rights © 2014 Brindle,All Rights Reserved.</p>
  <span class="social abs" style="left:643px"></span>
  <span class="social abs" style="left:671px"></span>
  <span class="social abs" style="left:701px"></span>
</footer>

</body>
</html>
```